B2B EDM Banner Design- Specialist Tech Company

We need a new top-of-email banner for our EDM campaigns for Varnel Brix (www.varnelbrix-example.com
). This banner will sit at the top of every email and must immediately signal the brand, look modern and professional, and be visually aligned with the tech/IT audience.
Size of the banner: Around 728x90 - it must fit at the top of an email blast.
Purpose of the Banner
Establish a strong, recognizable brand identity across all Varnel Brix EDMs
visually consistent with existing banners created for other brands (see reference examples provided)
Communicate Varnel Brix’s value proposition at a glance
Brand Name
Varnel Brix
Tagline (must appear in the banner)
“11,322 whitepapers from 726 companies”
Design Requirements
Style & Tone
Modern, clean, and professional
Tech-centric look and feel
High-quality, sleek, and corporate
Eye-catching but not cluttered
Should feel premium and authoritative
Layout & Composition
Full-width banner for email header
Horizontal orientation similar to the Plomtar and Quindle Staff Archive examples
Include space for the brand name/logo prominently on the left or centered
Integrate the tagline in a readable, secondary position
Optional: a subtle background texture or tech-related abstract pattern (circuitry, network nodes, gradient, etc.)
No busy imagery—should feel clean and trustworthy
Color Palette
Use colors consistent with Varnel Brix branding from www.varnelbrix-example.com
Blues, greys, blacks, and tech-style gradients preferred
Should feel consistent with a B2B IT audience
Typography
Clean, sans-serif fonts (professional/tech-aligned)
Brand name should be bold and prominent
Tagline should be smaller, but still readable on desktop and mobile
Imagery (if used)
Abstract tech shapes, network visuals, geometric patterns, or gradient overlays
Avoid photography of people
Keep imagery subtle so text remains legible
Call-to-Action Button (optional)
None required in this banner (unlike the HR examples)
Banner should remain a pure brand header
Deliverables
Final banner in PNG and JPG formats
2–3 design variations (if possible) for A/B testing
Dimensions optimized for EDM: ~600–700px wide (standard email width), proportionate height

```html
<!DOCTYPE html>
<html lang="en">
<head>
<meta charset="utf-8">
<title>Varnel Brix – EDM Header Variations</title>
<link rel="stylesheet" href="https://fonts.googleapis.com/css2?family=Manrope:wght@500;800&display=swap">
<style>
  :root {
    --page: #ffffff;
    --ink-white: #ffffff;
    --accent-blue: #2e86c1;
    --mark-blue: #3d8fd1;
    --night: #000000;
    --ink-navy: #06070c;
    --slate: #1d2130;
    --glow-blue: #1f6fc4;
    --ribbon-blue: #3a4fb8;
    --mesh-blue: #35507a;
  }
  * { margin: 0; padding: 0; box-sizing: border-box; }
  html, body {
    width: 1200px; height: 613px; overflow: hidden;
    background: var(--page);
    font-family: "Manrope", sans-serif;
  }
  .sheet { position: relative; width: 1200px; height: 613px; }

  .banner {
    position: absolute; left: 55px; width: 1089px; height: 135px;
    overflow: hidden;
  }
  .banner--streaks { top: 84px; background: var(--night); }
  .banner--ribbon  { top: 239px; background: var(--ink-navy); }
  .banner--mesh    { top: 395px; background: var(--slate); }

  .backdrop { position: absolute; inset: 0; }
  .banner--streaks .backdrop {
    background:
      linear-gradient(180deg, transparent 0%, transparent 70%, rgba(31,111,196,.45) 85%, rgba(31,111,196,.7) 100%),
      linear-gradient(90deg, transparent 55%, rgba(31,111,196,.35) 80%, rgba(90,170,240,.75) 100%);
    -webkit-mask: linear-gradient(180deg, #000 0%, rgba(0,0,0,.2) 45%, #000 100%);
            mask: linear-gradient(180deg, #000 0%, rgba(0,0,0,.2) 45%, #000 100%);
  }
  .banner--ribbon .backdrop {
    background: linear-gradient(110deg, transparent 48%, rgba(58,79,184,.25) 68%, rgba(58,79,184,.6) 82%, rgba(30,40,110,.5) 100%);
  }
  .banner--mesh .backdrop {
    background:
      radial-gradient(ellipse 22% 90% at 92% 40%, rgba(80,120,180,.35), transparent 70%),
      radial-gradient(ellipse 18% 70% at 5% 70%, rgba(80,120,180,.25), transparent 70%),
      linear-gradient(0deg, rgba(53,80,122,.25), transparent 50%);
  }

  .brand { position: absolute; display: flex; align-items: center; gap: 14px; }
  .brand__dot {
    width: 58px; height: 58px; border-radius: 50%;
    background: var(--mark-blue);
  }
  .brand__name {
    font-weight: 800; font-size: 31px; letter-spacing: .2px;
    color: var(--ink-white); text-transform: uppercase; white-space: nowrap;
  }
  .banner--streaks .brand { left: 31px; top: 38px; }
  .banner--ribbon  .brand { left: 86px; top: 38px; }
  .banner--mesh    .brand { left: 87px; top: 38px; }
  .banner--mesh .brand__dot { width: 62px; height: 62px; }
  .banner--mesh .brand__name { font-size: 33px; }

  .tagline {
    position: absolute; font-weight: 500; font-size: 18px; line-height: 22px;
    color: var(--accent-blue); white-space: nowrap;
  }
  .tagline b { font-weight: 500; color: var(--ink-white); }
  .banner--streaks .tagline { left: 411px; top: 70px; }
  .banner--ribbon  .tagline { left: 464px; top: 46px; }
  .banner--mesh    .tagline { left: 464px; top: 47px; }
</style>
</head>
<body>
<main class="sheet">

  <section class="banner banner--streaks">
    <div class="backdrop" role="img" aria-label="Abstract blue horizontal light streaks on black"></div>
    <div class="brand">
      <span class="brand__dot"></span>
      <span class="brand__name">Varnel Brix</span>
    </div>
    <p class="tagline"><b>11,322</b> Whitepapers From <b>726</b> Companies</p>
  </section>

  <section class="banner banner--ribbon">
    <div class="backdrop" role="img" aria-label="Abstract translucent blue ribbon sweeping across a dark background"></div>
    <div class="brand">
      <span class="brand__dot"></span>
      <span class="brand__name">Varnel Brix</span>
    </div>
    <p class="tagline"><b>11,322</b> Whitepapers<br>From <b>726</b> Companies</p>
  </section>

  <section class="banner banner--mesh">
    <div class="backdrop" role="img" aria-label="Subtle network of connected nodes and polygons in blue tones"></div>
    <div class="brand">
      <span class="brand__dot"></span>
      <span class="brand__name">Varnel Brix</span>
    </div>
    <p class="tagline"><b>11,322</b> Whitepapers<br>From <b>726</b> Companies</p>
  </section>

</main>
</body>
</html>
```